Business Card design which attached logo. Company is called Tallowind Shield and main colours are Orange & Black.

Company specialises in Paint Protection and Detailing for supercars.

Details needed on business card:

Sales

Address: Unit 14, 172 Garrick Road, Wexley Vale, NSW 2381

Phone: 02 9461 2738

website: www.tallowindshield.com.au

Email: sales@tallowindshield.com.au

```html
<!DOCTYPE html>
<html lang="en">
<head>
<meta charset="utf-8">
<title>Tallowind Shield — Business Card</title>
<link rel="stylesheet" href="https://fonts.googleapis.com/css2?family=Lato:wght@300;400&family=Ubuntu:wght@300;400&display=swap">
<style>
  :root {
    --page: #ffffff;
    --card: #0e1011;
    --orange: #f7390f;
    --ink: #111111;
    --white: #ffffff;
    --illustration-dark: #1a1615;
    --illustration-tint: #3a1b12;
    --illustration-grey: #2a2c2e;
  }
  html, body {
    margin: 0;
    padding: 0;
    width: 1040px;
    height: 1200px;
    overflow: hidden;
    background: var(--page);
  }
  .sheet {
    position: relative;
    width: 1040px;
    height: 1200px;
  }
  .card {
    position: absolute;
    left: 70px;
    width: 900px;
    height: 540px;
    background: var(--card);
    box-shadow: 0 1px 5px rgba(0,0,0,0.3);
    overflow: hidden;
  }
  .card--front { top: 33px; }
  .card--back { top: 614px; }

  .car-art {
    position: absolute;
    border-radius: 60px 80px 20px 20px;
  }
  .card--front .car-art {
    left: 142px; top: 123px; width: 616px; height: 156px;
    background: linear-gradient(180deg, var(--illustration-dark), var(--illustration-tint));
  }
  .card--back .car-art {
    left: 450px; top: 210px; width: 440px; height: 116px;
    background: linear-gradient(180deg, var(--illustration-dark), var(--illustration-grey));
  }

  .brand-band {
    position: absolute;
    left: 0; top: 283px;
    width: 900px; height: 121px;
    background: var(--orange);
    display: flex;
    align-items: center;
    justify-content: center;
  }
  .brand-band__name {
    font-family: "Lato", sans-serif;
    font-weight: 300;
    font-size: 38px;
    letter-spacing: 0.5px;
    color: var(--ink);
    text-transform: uppercase;
  }

  .frame {
    position: absolute;
    left: 0; top: 0;
    width: 900px; height: 540px;
  }

  .back-title {
    position: absolute;
    left: 48px; top: 104px;
    margin: 0;
    font-family: "Ubuntu", sans-serif;
    font-weight: 400;
    font-size: 46px;
    letter-spacing: 2px;
    color: var(--white);
    text-transform: uppercase;
    line-height: 1;
  }
  .title-rule {
    position: absolute;
    left: 48px; top: 168px;
    width: 109px; height: 10px;
    background: var(--white);
  }

  .contacts {
    position: absolute;
    left: 76px; top: 244px;
    margin: 0; padding: 0;
    list-style: none;
    font-family: "Ubuntu", sans-serif;
    font-weight: 300;
    color: var(--white);
  }
  .contacts__item {
    display: flex;
    align-items: flex-start;
    gap: 12px;
    font-size: 22px;
    line-height: 28px;
    letter-spacing: 0.6px;
  }
  .contacts__item + .contacts__item { margin-top: 12px; }
  .contacts__item--phone, .contacts__item--email, .contacts__item--web { font-size: 24px; }
  .contacts__item--email, .contacts__item--web { margin-top: 14px !important; }
  .contacts__icon {
    width: 22px; height: 26px;
    flex: none;
    margin-top: 1px;
  }
</style>
</head>
<body>
<main class="sheet">

  <section class="card card--front" aria-label="Card front">
    <div class="car-art" role="img" aria-label="Orange line drawing of a supercar in side profile"></div>
    <div class="brand-band">
      <span class="brand-band__name">Tallowind Shield</span>
    </div>
  </section>

  <section class="card card--back" aria-label="Card back">
    <svg class="frame" viewBox="0 0 900 540" aria-hidden="true">
      <path d="M0 64 H368 V52 Q451 30 535 52 V64 H900" fill="none" stroke="var(--white)" stroke-width="3"/>
      <path d="M0 466 H396 L452 500 L509 466 H900" fill="none" stroke="var(--white)" stroke-width="3"/>
    </svg>

    <h1 class="back-title">Tallowind Shield</h1>
    <div class="title-rule"></div>

    <ul class="contacts">
      <li class="contacts__item contacts__item--address">
        <svg class="contacts__icon" viewBox="0 0 22 26" aria-hidden="true">
          <path d="M11 1 C5.5 1 2 5 2 9.5 C2 15 11 25 11 25 C11 25 20 15 20 9.5 C20 5 16.5 1 11 1 Z" fill="var(--white)"/>
          <circle cx="11" cy="9.5" r="3.2" fill="var(--card)"/>
        </svg>
        <span>Unit 14, 172 Garrick Road<br>Wexley Vale, NSW 2381</span>
      </li>
      <li class="contacts__item contacts__item--phone">
        <svg class="contacts__icon" viewBox="0 0 22 26" aria-hidden="true">
          <path d="M4 3 L8 2 L10 8 L7.5 10 Q10 16 14.5 19 L17 17 L21 21 L19.5 24.5 Q9 24 3 10 Z" fill="var(--white)"/>
        </svg>
        <span>02 9461 2738</span>
      </li>
      <li class="contacts__item contacts__item--email">
        <svg class="contacts__icon" viewBox="0 0 22 26" aria-hidden="true">
          <text x="0" y="21" font-family="Ubuntu, sans-serif" font-size="24" fill="var(--white)">@</text>
        </svg>
        <span>sales@tallowindshield.com.au</span>
      </li>
      <li class="contacts__item contacts__item--web">
        <svg class="contacts__icon" viewBox="0 0 22 26" aria-hidden="true">
          <g fill="none" stroke="var(--white)" stroke-width="1.6">
            <circle cx="11" cy="13" r="9.5"/>
            <ellipse cx="11" cy="13" rx="4.2" ry="9.5"/>
            <path d="M1.5 13 H20.5 M3 8 H19 M3 18 H19"/>
          </g>
        </svg>
        <span>www.tallowindshield.com.au</span>
      </li>
    </ul>

    <div class="car-art" role="img" aria-label="White line drawing of a supercar in side profile"></div>
  </section>

</main>
</body>
</html>
```